Coffee House With Cycling Theme Wants Business Cards

We want to create a business card for a coffee house that has a cycling theme. We expect to use the current logo on one side of the business card and we have been considering adding the words 'COFFEE HOUSE' underneath (see example). For the other side of the business card we want an interesting design with tag-line, address and social media links (the normal business card stuff). See examples provided but we are not fixed on having it exactly as shown, we are very open to great creative ideas. Please note our logo has the initials ‘RM' in orange embedded in the design and this must be retained. However, you can play with the words COFFEE HOUSE as well as use the orange color on the backside of the business card, as you see fit. For an image on the backside of the business card it can be a photo, hand-drawn or whatever but it must visually combine coffee and cycling in some way. The interior of the Coffee House will be reclaimed wood, rustic and have an urban feel to it with cycling artifacts hanging from the walls/ceiling, etc. Finally, it would be beneficial if the business card design elements can be easily used on flyers and other promotional assets. Good luck, we are looking forward to seeing your creative ideas.

Target Market(s)

Coffee lovers and cycling fans

Contact Information for Business Card

See project description.

Colors

Designer to choose colors to be used in the design.

Requirements
Must have
• Must use the current logo provided and combine a coffee and bike theme.
Nice to have
• Orange is used in current logo and could be used as an accent color on the backside of the business card.

```html
<!DOCTYPE html>
<html lang="en">
<head>
<meta charset="utf-8">
<title>RM Coffee House – Business Card</title>
<link href="https://fonts.googleapis.com/css2?family=Open+Sans:ital,wght@0,400;0,600;1,400&display=swap" rel="stylesheet">
<style>
  :root{
    --bg:#1d2023;
    --orange:#f07a1a;
    --orange-light:#f59a2a;
    --espresso:#2a1a10;
    --ink:#0e0c0b;
    --white:#ffffff;
    --grey:#9a9a9a;
    --wood-dark:#1f2322;
    --wood-teal:#2f4440;
  }
  *{box-sizing:border-box;margin:0;padding:0}
  html,body{width:1200px;height:900px;overflow:hidden;background:var(--bg);font-family:"Open Sans",Arial,sans-serif}
  .canvas{position:relative;width:1200px;height:900px}
  .card{position:absolute;left:290px;width:620px;height:354px;border-radius:22px;overflow:hidden;box-shadow:0 14px 30px rgba(0,0,0,.45)}
  .card--info{top:58px;background:var(--ink)}
  .card--brand{top:488px;background:var(--wood-dark)}

  /* info side */
  .info-photo{position:absolute;inset:0;
    background:
      radial-gradient(ellipse 150px 115px at 440px 245px,#d9a04a 0%,#a8681f 45%,rgba(60,35,15,0) 100%),
      linear-gradient(135deg,var(--orange-light) 0%,var(--orange) 32%,#7a3c12 55%,var(--espresso) 72%,var(--ink) 100%)}
  .wordmark{position:absolute;font-weight:400;letter-spacing:2px;line-height:1}
  .info-wordmark{left:46px;top:32px;font-size:50px;color:var(--white)}
  .info-sub{position:absolute;left:46px;top:96px;font-size:20px;color:var(--white);letter-spacing:1px}
  .rule{position:absolute;left:46px;top:138px;width:250px;height:2px;background:var(--white)}
  .tagline{position:absolute;left:306px;top:126px;font-style:italic;font-size:17px;color:var(--white)}
  .person{position:absolute;left:46px;top:162px;color:var(--white);font-size:15px;font-weight:600}
  .person small{font-size:11px;font-weight:400;margin-left:6px}
  .contacts{position:absolute;left:46px;top:190px;list-style:none;color:var(--white);font-size:15px;line-height:23px}
  .contacts li{display:flex;align-items:center;gap:8px}
  .contacts li::before{content:"";width:9px;height:9px;border-radius:50%;border:1.5px solid var(--white)}
  .address{position:absolute;left:46px;bottom:26px;display:flex;align-items:center;gap:8px;color:var(--orange);font-size:20px}

  /* brand side */
  .brand-photo{position:absolute;inset:0;
    background:
      radial-gradient(ellipse 200px 130px at 170px 110px,#5a2e16 0%,#3a2014 50%,rgba(40,30,25,0) 100%),
      linear-gradient(160deg,var(--wood-teal) 0%,#2a302d 45%,var(--wood-dark) 75%,#141515 100%)}
  .brand-wordmark{right:86px;top:140px;font-size:62px;color:var(--orange)}
  .brand-sub{position:absolute;right:86px;top:222px;font-size:24px;color:var(--grey);letter-spacing:2px}
</style>
</head>
<body>
<main class="canvas">
  <section class="card card--info">
    <div class="info-photo" role="img" aria-label="Photo of hands holding a latte with leaf art on an orange-to-dark background"></div>
    <p class="wordmark info-wordmark">RM</p>
    <p class="info-sub">COFFEE HOUSE</p>
    <div class="rule"></div>
    <p class="tagline">Tagline tagline tagline tagline</p>
    <p class="person">YOUR NAME | <small>POSITION</small></p>
    <ul class="contacts">
      <li>rmcoffeehouse.com</li>
      <li>rmcoffeehouse</li>
      <li>rmcoffeehouse</li>
    </ul>
    <p class="address">
      <svg width="14" height="20" viewBox="0 0 14 20" aria-hidden="true"><path d="M7 0C3.1 0 0 3.1 0 7c0 5 7 13 7 13s7-8 7-13c0-3.9-3.1-7-7-7zm0 9.5A2.5 2.5 0 1 1 7 4.5a2.5 2.5 0 0 1 0 5z" fill="var(--orange)"/></svg>
      street address, street address
    </p>
  </section>

  <section class="card card--brand">
    <div class="brand-photo" role="img" aria-label="Photo of coffee beans, green leaves and a small espresso pot on weathered rustic wood"></div>
    <p class="wordmark brand-wordmark">RM</p>
    <p class="brand-sub">COFFEE HOUSE</p>
  </section>
</main>
</body>
</html>
```